Business Card Design Project

We need a business card design template for a direct sales company that is branded to the company but the name information can be changed for the representatives. The card needs to include the company logo and website...www.myvelsane.example. It should also include the Customer Service number which is 1-800-472-Velsan.

The front should have a space with the name and a place for their phone contact information and email address.
Updates

The card should be two sided.  It could also include the tagline "Velsane is all about V!" or any of the information from www.myvelsane.example.

I am uploading the other formats that I currently have for the logo.

Thank you

Target Market(s)

The representatives are teenage girls that are 13-19 but they are selling products to all ages.

Industry/Entity Type

Business

Requirements
Must have
• A field with the toll free customer service number.
The company logo.
The company website information.
The company representative name.
The company representative phone number.
The company representative email contact info.
Nice to have
• QR Code which we already have.
Should not have
• Do not make it look like a design for children. It should be modern and professional but sophisticated.

```html
<!DOCTYPE html>
<html lang="en">
<head>
<meta charset="utf-8">
<title>Velsane Business Card</title>
<link rel="stylesheet" href="https://fonts.googleapis.com/css2?family=Cinzel:wght@400;600&family=Montserrat:wght@500;600&display=swap">
<style>
  :root {
    --plum-center: #7b2d57;
    --plum-mid: #642545;
    --plum-edge: #471a30;
    --rose: #cc7aa6;
    --charcoal: #4a4646;
    --white: #ffffff;
    --soft-white: #f1dce8;
  }
  * { margin: 0; padding: 0; box-sizing: border-box; }
  html, body {
    width: 1200px;
    height: 778px;
    overflow: hidden;
    background: var(--plum-edge);
  }
  .card {
    position: relative;
    width: 1200px;
    height: 778px;
    background: radial-gradient(ellipse 60% 62% at 52% 34%, var(--plum-center) 0%, var(--plum-mid) 55%, var(--plum-edge) 100%);
  }
  .brand-name {
    position: absolute;
    left: 0;
    width: 1200px;
    top: 374px;
    text-align: center;
    font-family: "Cinzel", serif;
    font-weight: 600;
    font-size: 170px;
    line-height: 1;
    letter-spacing: 2px;
    color: var(--rose);
  }
  .website {
    position: absolute;
    right: 257px;
    top: 520px;
    font-family: "Montserrat", sans-serif;
    font-weight: 600;
    font-size: 22px;
    letter-spacing: 0.3px;
    color: var(--charcoal);
  }
  .website .domain { color: var(--rose); }
  .service-line {
    position: absolute;
    left: 0;
    width: 1200px;
    top: 574px;
    text-align: center;
    font-family: "Cinzel", serif;
    font-weight: 600;
    font-size: 34px;
    letter-spacing: 2px;
    color: var(--white);
  }
  .service-line .word { color: var(--rose); }
  .representative {
    position: absolute;
    left: 0;
    width: 1200px;
    top: 668px;
    text-align: center;
    font-family: "Montserrat", sans-serif;
    font-weight: 500;
    color: var(--soft-white);
  }
  .rep-name {
    font-family: "Cinzel", serif;
    font-weight: 600;
    font-size: 24px;
    letter-spacing: 1.5px;
    color: var(--rose);
  }
  .rep-contact {
    margin-top: 8px;
    font-size: 17px;
    letter-spacing: 0.5px;
  }
  .rep-contact .divider { color: var(--rose); padding: 0 14px; }
</style>
</head>
<body>
  <main class="card">
    <div class="brand-name">Velsane</div>
    <div class="website">www.<span class="domain">myvelsane</span>.example</div>
    <div class="service-line">1-800-472-<span class="word">Velsan</span></div>
    <section class="representative">
      <div class="rep-name">Mia Harlow</div>
      <div class="rep-contact">(555) 014-2287<span class="divider">|</span>mia.harlow@myvelsane.example</div>
    </section>
  </main>
</body>
</html>
```